Fundraising company advert in the industry magazine

KORBA Fundraising and KORBA Phone are sister fundraising companies, one specialising in street fundraising and one in tele-fundraising.

We need a simple joint advert that we can run in the industry magazine that lists off our services to new clients.

The advert is a third page ad (specs attached) and so we are not looking for something overly complicated but it must be on brand with previous adverts and the company colours of Red, Black on a white background. Variations will be considered if the advert can still be recognised as the KORBA Group.

MUST HAVE:

1) Company logos

2) The following content (placing of this content is not a concern as long as its clearly legible and the services of each company are visually associated with the logo);

KORBA Fundraising specialise in regular giving acquisition;

Face to Face Fundraising
Lead Generation
2-Step

Contact tom@korbafundraising.example / 02 7146 2519 / www.korbafundraising.example

KORBA Phone specialise in supporter acquisition and ongoing communications;

New Supporter Acquisition
Upgrades
Supporter Reactivation
Conversion to Regular Giving
Validation and Welcome Calls
Petition Conversion
Fulfilment Services
List Cleansing
Donor Journey Strategy

Contact gavin@korbaphone.example / 02 6482 1957 / www.korbaphone.example

Reason: Deadline extended due to personal medical issues and not had time to review designs. Apologies. Tom

Target Market(s)

Charities looking to invest budget in fundraising services

Industry/Entity Type

Industry

Requirements
Must have
• 1) Company logos

Face to Face Fundraising
Lead Generation
2-Step

New Supporter Acquisition
Upgrades
Supporter Reactivation
Petition Conversion
Fulfilment Services
List Cleansing
Donor Journey Strategy

```html
<!DOCTYPE html>
<html lang="en">
<head>
<meta charset="utf-8">
<title>KORBA Group – Joint Advert</title>
<link rel="stylesheet" href="https://fonts.googleapis.com/css2?family=Michroma&family=Source+Sans+3:wght@400;600&display=swap">
<style>
  :root {
    --red: #d3212a;
    --red-dark: #8e1418;
    --ink: #1c1c1c;
    --paper: #ffffff;
    --paper-shade: #e4e6e8;
    --stage: #ececec;
    --head-font: "Michroma", sans-serif;
    --body-font: "Source Sans 3", sans-serif;
  }
  * { box-sizing: border-box; margin: 0; padding: 0; }
  html, body { width: 1200px; height: 1000px; overflow: hidden; }
  body { background: var(--stage); font-family: var(--body-font); color: var(--ink); position: relative; }

  .advert {
    position: absolute; top: 255px; width: 560px; height: 490px;
    background: linear-gradient(135deg, var(--paper) 40%, var(--paper-shade) 100%);
    box-shadow: 0 6px 22px rgba(0,0,0,.18);
    overflow: hidden;
  }
  .advert--fundraising { left: 27px; }
  .advert--phone { left: 613px; }

  /* Fundraising advert */
  .frame {
    position: absolute; inset: 16px;
    border: 2px solid var(--red); border-radius: 30px;
  }
  .brand {
    display: flex; align-items: center; gap: 14px;
    font-family: var(--head-font); color: var(--red-dark);
    letter-spacing: 3px;
  }
  .brand__mark { width: 40px; height: 40px; background: var(--red-dark); border-radius: 4px; }
  .advert--fundraising .brand { position: absolute; left: 44px; top: 44px; font-size: 46px; }
  .headline {
    font-family: var(--head-font); color: var(--red);
    text-transform: uppercase; line-height: 1.35; letter-spacing: 1px;
  }
  .advert--fundraising .headline { position: absolute; left: 44px; top: 132px; font-size: 21px; }
  .service-list { list-style: none; font-size: 19px; }
  .advert--fundraising .service-list { position: absolute; left: 46px; top: 244px; }
  .advert--fundraising .service-list li { display: flex; align-items: center; gap: 10px; line-height: 34px; }
  .bullet-square { width: 18px; height: 14px; background: var(--red-dark); border-radius: 2px; }
  .device-shot {
    position: absolute; right: -30px; top: 250px; width: 290px; height: 200px;
    border-radius: 18px; border: 12px solid #111;
    background: linear-gradient(160deg, #f4f4f4 0%, #d9d2cc 45%, #c8432e 100%);
  }
  .advert--fundraising .contact {
    position: absolute; left: 46px; bottom: 36px; font-size: 15px; line-height: 22px;
  }
  .contact strong { font-weight: 600; }

  /* Phone advert */
  .top-band {
    position: absolute; left: 0; right: 0; top: 0; height: 14px;
    background: linear-gradient(90deg, var(--red-dark), var(--red));
  }
  .top-rule {
    position: absolute; left: 0; right: 0; top: 22px; height: 3px; background: var(--red-dark);
  }
  .advert--phone .brand {
    position: absolute; left: 0; right: 0; top: 70px; justify-content: center; font-size: 40px;
  }
  .brand__ring { width: 34px; height: 34px; border: 5px solid var(--red-dark); border-radius: 50%; }
  .advert--phone .headline { position: absolute; left: 32px; top: 220px; font-size: 20px; line-height: 1.45; }
  .advert--phone .service-list {
    position: absolute; right: 26px; top: 158px; text-align: right; font-size: 15px;
  }
  .advert--phone .service-list li { display: flex; justify-content: flex-end; align-items: center; gap: 8px; line-height: 27.5px; }
  .ring-icon { width: 13px; height: 13px; border: 2.5px solid var(--red); border-radius: 50%; flex: none; }
  .bottom-band {
    position: absolute; left: 0; right: 0; bottom: 0; height: 44px;
    background: linear-gradient(90deg, var(--red-dark), var(--red));
    display: flex; align-items: center; justify-content: center; gap: 18px;
    color: var(--paper); font-size: 14px;
  }
  .bottom-band span { display: flex; align-items: center; gap: 6px; }
  .bottom-band svg { width: 15px; height: 15px; }
</style>
</head>
<body>

<section class="advert advert--fundraising">
  <div class="frame"></div>
  <div class="brand"><span class="brand__mark"></span>KORBA</div>
  <h2 class="headline">KORBA Fundraising<br>specialise in regular<br>giving acquisition</h2>
  <ul class="service-list">
    <li><span class="bullet-square"></span>Face to Face Fundraising</li>
    <li><span class="bullet-square"></span>Lead Generation</li>
    <li><span class="bullet-square"></span>2-Step</li>
  </ul>
  <div class="device-shot" role="img" aria-label="Tablet showing the KORBA Fundraising website home page"></div>
  <p class="contact">tom@korbafundraising.example<br>02 7146 2519<br>www.<strong>korbafundraising</strong>.example</p>
</section>

<section class="advert advert--phone">
  <div class="top-band"></div>
  <div class="top-rule"></div>
  <div class="brand"><span class="brand__ring"></span>KORBA PHONE</div>
  <h2 class="headline">Specialise<br>in supporter<br>acquisition<br>and ongoing<br>communications</h2>
  <ul class="service-list">
    <li>New Supporter Acquisition<span class="ring-icon"></span></li>
    <li>Upgrades<span class="ring-icon"></span></li>
    <li>Supporter Reactivation<span class="ring-icon"></span></li>
    <li>Conversion to Regular Giving<span class="ring-icon"></span></li>
    <li>Validation and Welcome Calls<span class="ring-icon"></span></li>
    <li>Petition Conversion<span class="ring-icon"></span></li>
    <li>Fulfilment Services<span class="ring-icon"></span></li>
    <li>List Cleansing<span class="ring-icon"></span></li>
    <li>Donor Journey Strategy<span class="ring-icon"></span></li>
  </ul>
  <div class="bottom-band">
    <span>gavin@korbaphone.example</span>
    <span>
      <svg viewBox="0 0 16 16" aria-hidden="true"><rect x="4" y="1" width="8" height="14" rx="1.5" fill="none" stroke="#fff" stroke-width="1.5"/><rect x="6" y="3" width="4" height="6" fill="#fff"/></svg>
      02 6482 1957
    </span>
    <span>
      <svg viewBox="0 0 16 16" aria-hidden="true"><circle cx="8" cy="8" r="6.5" fill="none" stroke="#fff" stroke-width="1.3"/><ellipse cx="8" cy="8" rx="3" ry="6.5" fill="none" stroke="#fff" stroke-width="1.1"/><line x1="1.5" y1="8" x2="14.5" y2="8" stroke="#fff" stroke-width="1.1"/></svg>
      www.<strong>korbaphone</strong>.example
    </span>
  </div>
</section>

</body>
</html>
```